Business Card Project for 'Manufacturing and Healthcare Business Improvement company.

I need a business card for a consulting company that does process improvement for manufacturing and healthcare companies. I had a contest for a logo, and I liked what we came up with for the logo.

I wasn't blown away by what I got for the business card. The designer tried and it was a decent design, but I was looking for a little more. I want something that looks professional, but is eye-catching enough that people say "that looks cool, where did you get it?"

I've uploaded some business card examples I found that I liked. Even though some of the examples have red and orange on them, I think I would stick with blues, grays and blacks since that matches the logo theme. As awesome as some of them look, I don't think that a single color card, like an all-black card, will work for me; but feel free to change my mind.

It might also be possible to incorporate elements from the logo into the card. I also like some of the elements that use circles or rectangles etc to separate the phone number, website etc.

I like it when people have used geometric shapes to break up the card into sections or to add borders to the card to complement the logo, not compete with it for attention. For example, the red and gray example that has a curve that separates the card into two parts. I've wondered, how it would look if the red area were blue and had an arrow separating the top and bottom, like the arrow on the logo. Maybe on the back there could be an element that mirrors the bar graph and arrow. Would those look interesting, or would they compete with the other elements too much?

I also uploaded some examples of cards I made up, either based on ideas I saw elsewhere or based on design elements that the logo had in his designs. If you wonder why the ones with "lorem ipsum" look like an amateur did them, it's because they did.

I also think that I may add a QR code at some point, so I would need a location for that, along with something that says what the QR links to, such as, "scan here to upload contact information" or something similar. I don't know if I want cards that require having special designs cut, but if you have the idea, go with it.

I don't want to limit anyone's creativity, so I'll leave it at that.

Target Market(s)

Healthcare and Manufacturing

Industry/Entity Type

Manufacturing

Contact Information for Business Card

Harborline Advisory Partners LLC.
Gary Pruett MBA, LSSMBB
Managing Partner
g.pruett@harborlineadvisorypartnersllc.example
(555) 987-6240

Font styles to use
Serif
Sans Serif

Colors

Designer to choose only greyscale colors for use in the design.

Requirements
Must have
• The logo.
Nice to have
• Even though some of the examples I uploaded have red and orange on them, I think I would stick with blues, grays and blacks since that matches the logo theme.

I also like some of the elements that use circles or rectangles etc to separate the phone number, website etc.

I like it when people have used geometric shapes to break up the card into sections or to add borders to the card to complement the logo, not compete with it for attention.

For example, the red and gray example that has a curve that separates the card into two parts. I've wondered, how it would look if the red area were blue and had an arrow separating the top and bottom, like the arrow on the logo. Maybe on the back there could be an element that mirrors the bar graph and arrow. Would those look interesting, or would they compete with the other elements too much?

It might also be possible to incorporate elements from the logo into the card.

I also think that I may add a QR code at some point, so I would need a location for that, along with something that says what the QR links to, such as, "scan here to upload contact information" or something similar.

It could have something somewhere saying "We use Lean, Six Sigma and TPM continuous improvement tools to improve manufacturing and healthcare businesses."
Should not have
• So many colors and elements that it is distracting. Should not be generic.

As awesome as some of them look, I don't think that a single color card, like an all-black card, will work for me; but feel free to change my mind.

I don't know if I want cards that require having special designs cut, but if you have the idea, go with it.

```html
<!DOCTYPE html>
<html lang="en">
<head>
<meta charset="utf-8">
<title>Harborline Advisory Partners – Business Card</title>
<link href="https://fonts.googleapis.com/css2?family=Work+Sans:wght@400;500;700&display=swap" rel="stylesheet">
<style>
  :root {
    --navy: #1d3566;
    --navy-deep: #172c57;
    --steel: #7a7c80;
    --paper: #ffffff;
    --mist: #eef0f5;
    --ink: #4a4c52;
    --backdrop: #b9babc;
  }
  * { box-sizing: border-box; margin: 0; padding: 0; }
  html, body { width: 1200px; height: 930px; overflow: hidden; }
  body {
    background: var(--backdrop);
    font-family: "Work Sans", sans-serif;
    position: relative;
  }
  .card {
    position: absolute;
    width: 520px;
    height: 300px;
    border-radius: 18px;
    overflow: hidden;
  }
  /* Back side */
  .card--back {
    left: 70px; top: 110px;
    background: var(--navy);
    color: var(--paper);
  }
  .card--back .brand {
    position: absolute;
    left: 0; right: 0; top: 92px;
    text-align: center;
    font-size: 26px;
    font-weight: 700;
    letter-spacing: 0.5px;
    line-height: 1.2;
    color: var(--paper);
  }
  .card--back .tagline {
    position: absolute;
    left: 40px; right: 40px; bottom: 40px;
    text-align: center;
    font-size: 14px;
    letter-spacing: 0.6px;
    line-height: 1.45;
  }
  /* Front side */
  .card--front {
    left: 610px; top: 500px;
    background: var(--paper);
    color: var(--ink);
  }
  .card--front .accent {
    position: absolute; inset: 0;
  }
  .card--front .content {
    position: absolute;
    left: 0; width: 390px; top: 34px;
    text-align: center;
  }
  .card--front .brand {
    font-size: 17px;
    font-weight: 700;
    color: var(--navy);
    line-height: 1.2;
  }
  .card--front .person {
    margin-top: 22px;
    font-size: 19px;
    font-weight: 700;
    letter-spacing: 1px;
    text-transform: uppercase;
    color: var(--navy);
  }
  .card--front .role {
    margin-top: 4px;
    font-size: 12px;
  }
  .rule {
    width: 310px;
    height: 1px;
    background: var(--navy);
    margin: 10px auto;
  }
  .card--front .detail {
    font-size: 12px;
    line-height: 1.6;
  }
</style>
</head>
<body>
  <section class="card card--back">
    <div class="brand">Harborline Advisory<br>Partners LLC.</div>
    <p class="tagline">We use Lean, Six Sigma and TPM continuous improvement tools to improve manufacturing and healthcare businesses</p>
  </section>

  <section class="card card--front">
    <svg class="accent" width="520" height="300" viewBox="0 0 520 300" aria-hidden="true">
      <polygon points="400,0 520,0 520,300 330,300" fill="var(--mist)"/>
      <polygon points="470,240 520,215 520,300 430,300" fill="var(--navy)"/>
    </svg>
    <div class="content">
      <div class="brand">Harborline Advisory<br>Partners LLC.</div>
      <div class="person">Daniel Whitcombe</div>
      <div class="role">Managing Partner (Gary Pruett MBA, LSSMBB)</div>
      <div class="rule"></div>
      <div class="detail">127 Alder Creek Lane Reno, NV 89501</div>
      <div class="detail">P: (555) 987-6240</div>
      <div class="rule"></div>
      <div class="detail">E: g.pruett@harborlineadvisorypartnersllc.example</div>
    </div>
  </section>
</body>
</html>
```